Etiketten für Supplements
Zielgruppe
Verkauf von Supplements für einen gesunden Lifestyle
Aufgabenstellung
Grundlayout ist bei allen gleich
EU Richtlinien müssen nur eingehalten werden.
✅ Pflichtangaben auf einem Supplement-Etikett (EU-weit):
1. Verkehrsbezeichnung
z. B.: „Nahrungsergänzungsmittel mit Zink“
2. Nettofüllmenge
z. B.: „Inhalt: 90 Kapseln“
3. Verzehrempfehlung
z. B.: „Täglich 1 Kapsel mit ausreichend Flüssigkeit einnehmen.“ (unterschiedlich je nach Produkt erläutere ich unten weiter)
4. Zutatenliste (inkl. Kapselhülle & Zusatzstoffe)
Reihenfolge: mengenmäßig absteigend
5. Nährwerttabelle
Nährstoffangaben pro Tagesdosis
inkl. %NRV (Nutrient Reference Value, ehemals RDA)
6. Sicherheitshinweis
z. B.:
Nahrungsergänzungsmittel sind kein Ersatz für eine ausgewogene und abwechslungsreiche Ernährung sowie eine gesunde Lebensweise.
Die empfohlene tägliche Verzehrmenge darf nicht überschritten werden.
Außerhalb der Reichweite von kleinen Kindern aufbewahren.
7. Lagerhinweise
Trocken, verschlossen und vor Sonnenlicht geschützt lagern.
8. Mindesthaltbarkeitsdatum & LOT-Nr.
Mindestens haltbar bis: siehe Boden
LOT-Nr.: [Nummer]
9. Name und Adresse des Inverkehrbringers
Blue Orasent
Lindenhofweg 14
63118 Offenbach, Deutschland
Design wie es ungefähr aussehen sollte schicke ich im Anhang. Anzahl der Kapseln sollte stehen 90 Vegane Kapseln , dass es hochdosiert ist. Made in Germany 190x70mm sind die Maße. Ich habe auch im Anhang ein anderes geschickt es sollte professionell aussehen wie das.
Grundlayout beendet:
Produkt 1:
Magnesiumbiglyscinat:
???? 4 klare Benefits (EU-konform formuliert):
Trägt zur normalen Funktion des Nervensystems bei
Unterstützt eine normale Muskelfunktion
Hilft, Müdigkeit und Erschöpfung zu reduzieren
Trägt zur Erhaltung normaler Knochen und Zäh..

```html
<!DOCTYPE html>
<html lang="de">
<head>
<meta charset="utf-8">
<title>Vitamin C – Etikett</title>
<link href="https://fonts.googleapis.com/css2?family=Arimo:wght@400;700&family=Oswald:wght@500;600&family=Roboto+Condensed:wght@400;800&display=swap" rel="stylesheet">
<style>
  :root{
    --stage:#3ba6a8;
    --label-top:#37a3a6;
    --label-bottom:#6cb07c;
    --ink:#1f1f1f;
    --ink-soft:#3b3b3b;
    --white:#ffffff;
    --white-soft:rgba(255,255,255,.88);
    --rule:rgba(255,255,255,.7);
    --accent:#e8892b;
    --brand-blue:#3c8fd6;
    --brand-green:#2f9e5a;
    --tick:#2e9a5c;
    --leaf-area:rgba(255,255,255,.10);
  }
  *{box-sizing:border-box;margin:0;padding:0}
  html,body{width:1200px;height:675px;overflow:hidden}
  body{background:var(--stage);font-family:"Arimo",Arial,sans-serif;position:relative}

  .label{
    position:absolute;left:40px;top:131px;width:1120px;height:412px;
    background:linear-gradient(180deg,var(--label-top) 0%,var(--label-bottom) 100%);
    color:var(--white);overflow:hidden;
  }

  .text-block{position:absolute;font-size:11.6px;line-height:15.4px;color:var(--white-soft)}
  .text-block h3{font-size:11.8px;font-weight:700;color:var(--white)}
  .col-left{left:20px;width:264px}
  .col-left p{text-align:justify}
  .col-right{left:836px;width:264px}
  .divider{position:absolute;left:20px;top:72px;width:264px;border-top:1px solid var(--rule)}

  /* areas reserved for the leaf artwork */
  .leaf-area{position:absolute;background:var(--leaf-area);border-radius:4px}
  .leaf-area-left{left:312px;top:25px;width:105px;height:130px}
  .leaf-area-right{left:697px;top:25px;width:97px;height:110px}

  .hero-shape{position:absolute;left:358px;top:31px}

  .brand{position:absolute;left:410px;width:300px;top:58px;text-align:center}
  .brand-dot{display:block;width:40px;height:40px;border-radius:50%;background:var(--brand-blue);margin:0 auto}
  .brand-name{display:block;margin-top:14px;font-weight:700;font-size:12px;letter-spacing:1.4px;color:var(--brand-green)}

  .product-name{
    position:absolute;left:360px;width:400px;top:146px;text-align:center;
    font-family:"Roboto Condensed",sans-serif;font-weight:800;font-size:70px;line-height:70px;
    color:var(--ink);letter-spacing:.5px;
  }
  .product-name .accent{color:var(--accent)}
  .product-form{
    position:absolute;left:419px;width:279px;top:215px;height:24px;
    background:var(--accent);color:var(--white);text-align:center;
    font-family:"Oswald",sans-serif;font-weight:600;font-size:17.5px;line-height:24px;letter-spacing:.3px;
  }
  .benefits{
    position:absolute;left:410px;width:300px;top:245px;list-style:none;text-align:center;
    font-family:"Roboto Condensed",sans-serif;font-size:10px;line-height:17.5px;color:var(--ink-soft);
  }
  .benefits li::before{content:"✔";color:var(--tick);font-size:9px;margin-right:5px}

  .pack-size{
    position:absolute;left:359px;width:400px;top:370px;text-align:center;
    font-family:"Oswald",sans-serif;font-weight:500;font-size:19px;line-height:26px;color:var(--white);
  }

  .col-right .designation{text-align:justify}
  .col-right strong{color:var(--white)}
  .nutrition{width:100%;border-collapse:collapse;font-size:9px;line-height:12px}
  .nutrition th{font-weight:700;text-align:left;padding:3px 0 7px;border-bottom:1px solid var(--rule);color:var(--white)}
  .nutrition td{padding:8px 0;border-bottom:1px solid var(--rule)}
  .nutrition .first{width:88px}
  .nutrition .num{text-align:right}
  .footnote{font-size:9px;line-height:14px;text-align:justify}

  .origin-badge{
    position:absolute;left:1047px;top:332px;width:53px;height:61px;
    border:2px solid var(--white);border-radius:5px;background:rgba(255,255,255,.25);
  }
</style>
</head>
<body>
<section class="label">

  <div class="text-block col-left" style="top:18px">
    <h3>Verzehrempfehlung</h3>
    <p>Täglich 1 Kapsel mit ausreichend Wasser einnehmen, vorzugsweise zu einer Mahlzeit.</p>
  </div>
  <div class="divider"></div>
  <div class="text-block col-left" style="top:78px">
    <h3>Zutaten</h3>
    <p>Calciumascorbat, Hydroxypropylmethylcellulose (Kapselhülle), Mikrokristalline Cellulose (Füllstoff)</p>
  </div>
  <div class="text-block col-left" style="top:144px">
    <h3>Health Claims (EU-1924/2006)</h3>
    <p>Trägt zu einer normalen Funktion des Immunsystems bei.<br>
    Schützt die Zellen vor oxidativem Stress.<br>
    Trägt zur normalen Kollagenbildung bei – wichtig für Haut, Knochen, Zähne, Knorpel und Blutgefäße.<br>
    Hilft, Müdigkeit und Erschöpfung zu reduzieren.</p>
  </div>
  <div class="text-block col-left" style="top:272px">
    <h3>Sicherheitshinweise</h3>
    <p>Nahrungsergänzungsmittel sind kein Ersatz für eine ausgewogene und abwechslungsreiche Ernährung sowie eine gesunde Lebensweise.<br>
    Die empfohlene tägliche Verzehrmenge darf nicht überschritten werden.<br>
    Außerhalb der Reichweite von kleinen Kindern aufbewahren.</p>
  </div>

  <div class="leaf-area leaf-area-left" role="img" aria-label="Fläche für Blatt-Illustration"></div>
  <div class="leaf-area leaf-area-right" role="img" aria-label="Fläche für Blatt-Illustration"></div>

  <svg class="hero-shape" width="455" height="328" viewBox="0 0 455 328" aria-hidden="true">
    <path d="M228 4 C330 2 440 40 450 140 C458 240 380 324 232 325 C100 326 8 270 4 165 C0 62 110 6 228 4 Z" fill="#ffffff"/>
  </svg>

  <div class="brand">
    <span class="brand-dot"></span>
    <span class="brand-name">BLUE ORASENT</span>
  </div>
  <h1 class="product-name">VITAMIN <span class="accent">C</span></h1>
  <div class="product-form">GEPUFFERTES CALCIUMASCORBAT</div>
  <ul class="benefits">
    <li>Trägt zu einer normalen Funktion des Immunsystems bei</li>
    <li>Trägt dazu bei, die Zellen vor oxidativem Stress zu schützen</li>
    <li>Trägt zur Verringerung von Müdigkeit und Ermüdung</li>
    <li>Unterstützt die normale Kollagenbildung für Knochen, Knorpel,<br>Zähne, Zahnfleisch und Haut</li>
  </ul>

  <p class="pack-size">90 VEGAN KAPSELN = 100G℮ - HOCHDOSIERT</p>

  <div class="text-block col-right" style="top:18px">
    <p class="designation">Nahrungsergänzungsmittel mit <strong>Vitamin C (Calciumascorbat)</strong> – gepufferte, magenfreundliche Form</p>
  </div>
  <div class="text-block col-right" style="top:71px">
    <h3>Nährwerttabelle (pro Tagesdosis = 1 Kapsel)</h3>
  </div>
  <div class="text-block col-right" style="top:94px">
    <table class="nutrition">
      <tr><th class="first">Nährstoff</th><th>Menge pro 1 Kapsel</th><th class="num">% NRV*</th></tr>
      <tr><td class="first">Vitamin C</td><td>500 mg</td><td class="num">625%</td></tr>
    </table>
  </div>
  <div class="text-block col-right" style="top:148px">
    <p class="footnote">* NRV = Nährstoffbezugswerte gemäß EU-Verordnung 1169/2011</p>
  </div>
  <div class="text-block col-right" style="top:191px">
    <h3>Lagerhinweise</h3>
    <p>Trocken, verschlossen und vor Sonnenlicht geschützt lagern.</p>
  </div>
  <div class="text-block col-right" style="top:243px">
    <p>Mindestens haltbar bis: siehe Boden<br>LOT-Nr.: [Nummer]</p>
  </div>
  <div class="text-block col-right" style="top:280px">
    <h3>Inverkehrbringer</h3>
    <p>[Name &amp; Adresse des Kunden]</p>
  </div>

  <div class="origin-badge" role="img" aria-label="Herkunftssiegel"></div>
</section>
</body>
</html>
```